Velmora Care! Create an exciting flyer for our hemodialysis clinic

Create an engaging Flyer that shows our offering and that will drive patients to our hemodialysis clinic. www.velmoracare.example

Target Market(s)

Mass public

Industry/Entity Type

Healthcare

Requirements
Must have
• 1 Our logo. 2. Should include that we accept all insurances 3. Our tag line “Transforming Lives, One Dialysis Session at a Time.”

```html
<!DOCTYPE html>
<html lang="en">
<head>
<meta charset="utf-8">
<title>Velmora Care – Hemodialysis Flyer</title>
<link rel="stylesheet" href="https://fonts.googleapis.com/css2?family=Cabin+Condensed:wght@700&family=Questrial&family=Arimo&family=Montserrat:wght@700&display=swap">
<style>
  :root {
    --brand-blue: #2b7cc6;
    --brand-green: #4a9d2c;
    --headline-navy: #0f3f7d;
    --body-grey: #454545;
    --button-dark: #3e434a;
    --paper: #ffffff;
    --photo-light: #e4ecf1;
    --photo-mid: #b9cad6;
    --photo-deep: #8ea6b8;
  }
  html, body {
    margin: 0;
    padding: 0;
    width: 887px;
    height: 1200px;
    overflow: hidden;
    background: var(--paper);
  }
  .flyer {
    position: relative;
    width: 887px;
    height: 1200px;
    background: var(--paper);
    overflow: hidden;
  }
  .flyer svg.artwork {
    position: absolute;
    inset: 0;
  }
  .tagline {
    position: absolute;
    left: 387px;
    top: 42px;
    margin: 0;
    font-family: "Cabin Condensed", sans-serif;
    font-weight: 700;
    font-size: 44px;
    line-height: 58px;
    color: var(--headline-navy);
    text-transform: uppercase;
    white-space: nowrap;
  }
  .tagline .mark {
    font-size: 50px;
    line-height: 0;
    vertical-align: 8px;
  }
  .tagline .mark.open {
    position: absolute;
    left: -42px;
    top: 24px;
  }
  .insurance {
    position: absolute;
    left: 244px;
    top: 0;
    width: 200px;
    height: 1200px;
    font-family: "Questrial", sans-serif;
    color: var(--brand-green);
    line-height: 1;
    pointer-events: none;
  }
  .insurance span {
    position: absolute;
    left: 0;
    width: 200px;
    text-align: center;
    white-space: nowrap;
  }
  .insurance .accept { top: 633px; font-size: 48px; }
  .insurance .all { top: 675px; font-size: 76px; }
  .insurance .insurances { top: 747px; font-size: 29px; }
  .contact-band {
    position: absolute;
    right: 33px;
    top: 654px;
    text-align: right;
    color: var(--paper);
    font-family: "Questrial", sans-serif;
    font-weight: 700;
    white-space: nowrap;
  }
  .contact-band .phone { font-size: 32px; font-family: "Montserrat", sans-serif; display: block; line-height: 38px; }
  .contact-band .email { font-size: 23px; display: block; margin-top: 2px; }
  .service-copy {
    position: absolute;
    right: 42px;
    top: 781px;
    margin: 0;
    text-align: right;
    font-family: "Arimo", sans-serif;
    font-size: 18px;
    line-height: 28.6px;
    color: var(--body-grey);
    white-space: nowrap;
  }
  .book-button {
    position: absolute;
    left: 525px;
    top: 985px;
    width: 313px;
    height: 60px;
    border-radius: 9px;
    background: var(--button-dark);
    color: var(--paper);
    font-family: "Montserrat", sans-serif;
    font-weight: 700;
    font-size: 46px;
    line-height: 60px;
    text-align: center;
    text-decoration: none;
  }
  .address {
    position: absolute;
    right: 50px;
    top: 1060px;
    margin: 0;
    text-align: right;
    font-family: "Questrial", sans-serif;
    font-size: 22px;
    line-height: 32px;
    color: var(--body-grey);
    white-space: nowrap;
  }
  .website {
    position: absolute;
    right: 49px;
    top: 1122px;
    font-family: "Questrial", sans-serif;
    font-weight: 700;
    font-size: 28px;
    color: var(--brand-blue);
    text-decoration: none;
    white-space: nowrap;
  }
  .brand {
    position: absolute;
    left: 62px;
    top: 895px;
    width: 300px;
    text-align: center;
    font-family: "Questrial", sans-serif;
    color: var(--brand-blue);
  }
  .brand .brand-square {
    display: block;
    margin: 0 auto;
    width: 141px;
    height: 141px;
    box-sizing: border-box;
    border: 6px solid var(--brand-blue);
  }
  .brand .brand-name {
    display: block;
    font-size: 60px;
    line-height: 1;
    margin-top: 14px;
    letter-spacing: 1px;
  }
  .brand .brand-sub {
    display: block;
    font-size: 32px;
    line-height: 1;
    margin-top: 6px;
    letter-spacing: 3px;
  }
</style>
</head>
<body>
<main class="flyer">
  <svg class="artwork" width="887" height="1200" viewBox="0 0 887 1200" xmlns="http://www.w3.org/2000/svg">
    <defs>
      <linearGradient id="photoTone" x1="0" y1="0" x2="1" y2="1">
        <stop offset="0" stop-color="#eef2f5"/>
        <stop offset="0.6" stop-color="#c9d6df"/>
        <stop offset="1" stop-color="#9db2c2"/>
      </linearGradient>
      <linearGradient id="roomTone" x1="0" y1="0" x2="0" y2="1">
        <stop offset="0" stop-color="#f1f3f4"/>
        <stop offset="1" stop-color="#d3c4b6"/>
      </linearGradient>
      <linearGradient id="nurseTone" x1="0" y1="0" x2="1" y2="1">
        <stop offset="0" stop-color="#e3eaf0"/>
        <stop offset="1" stop-color="#6f9cd2"/>
      </linearGradient>
    </defs>

    <polygon class="hero-photo" role="img" aria-label="Photo: a nurse checks the blood pressure of an older patient resting in a clinic bed"
      points="53,0 887,0 887,642 583,617 378,613 325,503 237,343" fill="url(#photoTone)"/>

    <polygon class="accent-stripe green" points="32,0 57,0 237,343 211,343" fill="var(--brand-green)"/>
    <polygon class="accent-stripe blue" points="19,77 53,40 207,351 156,355" fill="var(--brand-blue)"/>
    <polygon class="accent-stripe green" points="57,286 92,245 147,363 109,392" fill="var(--brand-green)"/>

    <polygon class="contact-band-shape" points="583,617 887,642 887,744 456,744" fill="var(--brand-green)"/>

    <circle cx="215" cy="458" r="116" fill="var(--paper)"/>
    <circle class="room-photo" role="img" aria-label="Photo: bright dialysis room with treatment beds" cx="215" cy="458" r="108" fill="url(#roomTone)" stroke="var(--brand-blue)" stroke-width="5"/>
    <circle cx="132" cy="638" r="105" fill="var(--paper)"/>
    <circle class="staff-photo" role="img" aria-label="Photo: clinician in scrubs operating a dialysis machine" cx="132" cy="638" r="98" fill="url(#nurseTone)" stroke="var(--brand-blue)" stroke-width="5"/>

    <polygon class="star-point" points="339,507 295,601 386,601" fill="var(--brand-blue)"/>
    <polygon class="star-point" points="438,621 545,630 463,703" fill="var(--brand-blue)"/>
    <polygon class="star-point" points="203,867 301,820 241,765" fill="var(--brand-blue)"/>
    <polygon class="star-point" points="369,820 465,871 442,771" fill="var(--brand-blue)"/>
  </svg>

  <h1 class="tagline"><span class="mark open">“</span>Transforming Lives<br>One Dialysis Session<br>At A Time <span class="mark">”</span></h1>

  <div class="insurance">
    <span class="accept">ACCEPT</span>
    <span class="all">ALL</span>
    <span class="insurances">INSURANCES</span>
  </div>

  <div class="contact-band">
    <span class="phone">555-014-3239</span>
    <span class="email">info@velmoracare.example</span>
  </div>

  <p class="service-copy">We offer In-center hemodialysis for renal<br>patients who prefer to have their treat-<br>ments at a dialysis center.<br>Our dialysis center has 6 Kestrel<br>dialysis machines, supported by our state<br>of the art water purification system.</p>

  <a class="book-button" href="#">Book Now</a>

  <p class="address">14 Linden Walk, Off Harrowmere<br>Road, Eastvale, Mt. Corran</p>
  <a class="website" href="#">www.velmoracare.example</a>

  <div class="brand">
    <span class="brand-square"></span>
    <span class="brand-name">VELMORA</span>
    <span class="brand-sub">CARE</span>
  </div>
</main>
</body>
</html>
```